Label for Gin Bottle - Cranberry & Peach

Hi, We have created a Cranberry & Peach Gin that we require a label for.
The gin will be a vivid Orange/red colour in a clear 50cl bottle
The gin will be 40% Vol.
I am looking for a classy design with a summer/fresh appearance.
Thank You.

```html
<!DOCTYPE html>
<html lang="en">
<head>
<meta charset="utf-8">
<title>Cranberry &amp; Peach Gin Label</title>
<link rel="stylesheet" href="https://fonts.googleapis.com/css2?family=Playfair+Display+SC:wght@700&family=Libre+Baskerville:wght@400;700&display=swap">
<style>
  :root {
    --backdrop: #c9d0da;
    --navy: #272b3a;
    --gold: #c9a24a;
    --gold-light: #f0d58a;
    --gold-dark: #8e6a22;
    --bloom-crimson: #b4244c;
    --bloom-pink: #ec7d95;
    --bloom-peach: #f6cdb3;
    --leaf-plum: #6f5a78;
  }
  * { box-sizing: border-box; margin: 0; padding: 0; }
  html, body {
    width: 794px; height: 1200px; overflow: hidden;
    background: var(--backdrop);
  }
  .canvas {
    position: relative; width: 794px; height: 1200px;
    display: flex; align-items: center; justify-content: center;
  }
  .label {
    position: relative; width: 700px; height: 884px;
    background: var(--navy);
    overflow: hidden;
  }
  .label-frame {
    position: absolute; inset: 0; width: 100%; height: 100%;
    pointer-events: none; z-index: 3;
  }
  .floral-panel {
    position: absolute; left: 0; top: 0; bottom: 0; width: 278px;
    background:
      radial-gradient(circle at 30% 15%, var(--bloom-peach) 0 18%, transparent 40%),
      radial-gradient(circle at 75% 35%, var(--bloom-crimson) 0 14%, transparent 34%),
      radial-gradient(circle at 25% 55%, var(--leaf-plum) 0 12%, transparent 34%),
      radial-gradient(circle at 70% 70%, var(--bloom-peach) 0 14%, transparent 36%),
      radial-gradient(circle at 40% 90%, var(--bloom-crimson) 0 16%, transparent 38%),
      linear-gradient(180deg, var(--bloom-pink), #d9637f 50%, var(--bloom-pink));
  }
  .ornament {
    position: absolute; left: 318px; top: 0; width: 380px; height: 290px;
    background: radial-gradient(ellipse at 65% 25%, rgba(201,162,74,0.28), rgba(201,162,74,0.06) 60%, transparent 75%);
  }
  .label-copy {
    position: absolute; left: 278px; right: 0; top: 0; bottom: 0;
    text-align: center;
  }
  .label-copy > * { line-height: 1; white-space: nowrap; }
  .gold-text {
    background: linear-gradient(180deg, var(--gold-light), var(--gold) 45%, var(--gold-dark));
    -webkit-background-clip: text; background-clip: text;
    color: transparent;
  }
  .flavour {
    position: absolute; top: 368px; left: 0; right: 0;
    font-family: "Playfair Display SC", serif; font-weight: 700;
    font-size: 33px; letter-spacing: -0.8px;
  }
  .spirit {
    position: absolute; top: 428px; left: 0; right: 0;
    font-family: "Playfair Display SC", serif; font-weight: 700;
    font-size: 80px; letter-spacing: 2px;
  }
  .batch-box {
    position: absolute; top: 596px; left: 38px; width: 346px; height: 62px;
    border: 2px solid var(--gold); border-radius: 4px;
    display: flex; align-items: center; justify-content: center;
  }
  .abv {
    position: absolute; top: -13px; left: 50%; transform: translateX(-50%);
    background: linear-gradient(180deg, var(--gold-light), var(--gold));
    color: var(--navy);
    font-family: "Libre Baskerville", serif; font-size: 14px; font-weight: 700;
    padding: 3px 10px; border-radius: 3px; line-height: 1.2;
  }
  .batch {
    font-family: "Libre Baskerville", serif; font-size: 15px; font-weight: 700;
    color: var(--gold); margin-top: 6px;
  }
  .origin {
    position: absolute; top: 694px; left: 0; right: 0;
    font-family: "Libre Baskerville", serif; font-size: 13px;
    color: var(--gold);
  }
  .volume {
    position: absolute; top: 818px; left: 0; right: 0;
    font-family: "Libre Baskerville", serif; font-weight: 700; font-size: 28px;
  }
</style>
</head>
<body>
<main class="canvas">
  <article class="label">
    <div class="floral-panel" role="img" aria-label="Illustrated pattern of peach, pink and crimson flowers with plum leaves"></div>
    <div class="ornament" role="img" aria-label="Gold line-art mandala ornament"></div>
    <section class="label-copy">
      <h2 class="flavour gold-text">Cranberry &amp; Peach</h2>
      <h1 class="spirit gold-text">GIN</h1>
      <div class="batch-box">
        <span class="abv">40% VOL</span>
        <p class="batch">Premium Small Batch Production</p>
      </div>
      <p class="origin">Product of Country Name</p>
      <p class="volume gold-text">50 cl</p>
    </section>
    <svg class="label-frame" viewBox="0 0 700 884" aria-hidden="true">
      <rect x="7" y="7" width="686" height="870" fill="none" stroke="#c9a24a" stroke-width="12" stroke-dasharray="7 5"/>
      <rect x="15" y="15" width="670" height="854" fill="none" stroke="#8e6a22" stroke-width="2"/>
    </svg>
  </article>
</main>
</body>
</html>
```